TLB Feedback sticker

We need a sticker design for our secondary school (aged 11 - 18). This is to allow teachers to provide feedback to students and vice-versa, having a conversation with the learner. I would love to have at least two different designs and it to be attractive, so that all can be included. I've attached the basic outline with the information to be presented. It should be A5 size, so that 2 of these can be fitted in.

Target Market(s)

Secondary school students

Industry/Entity Type

School

Font styles to use
Sans Serif

Requirements
Must have
• Attached details of the headings and enough space for all parties to respond.
Should not have
• Anything deemed inappropriate for secondary students

```html
<!DOCTYPE html>
<html lang="en">
<head>
<meta charset="utf-8">
<title>Formative Feedback Sticker</title>
<link rel="stylesheet" href="https://fonts.googleapis.com/css2?family=Montserrat:wght@700&family=Arimo:wght@400&display=swap">
<style>
  :root {
    --backdrop: #ffffff;
    --frame: #f3ab70;
    --paper: #fdf1e0;
    --paper-light: #fef6ea;
    --rule: #ecdcc7;
    --binding: #f3a05e;
    --ink: #2a2420;
    --arc: #f0a060;
    --flag-tone-a: #8fc7a0;
    --flag-tone-b: #f6bc7e;
  }
  * { margin: 0; padding: 0; box-sizing: border-box; }
  html, body {
    width: 1200px; height: 821px; overflow: hidden;
    background: var(--backdrop);
  }
  .sticker {
    position: absolute; left: 331px; top: 30px;
    width: 538px; height: 760px;
    background: var(--frame);
  }
  .sheet {
    position: absolute; left: 31px; top: 47px;
    width: 472px; height: 670px;
    background-color: var(--paper);
    background-image: repeating-linear-gradient(
      to bottom,
      transparent 0, transparent 20.5px,
      var(--rule) 20.5px, var(--rule) 21.5px);
    background-position: 0 40px;
    overflow: hidden;
  }
  .header-arc { position: absolute; left: 0; top: 0; width: 472px; height: 120px; }
  .binding { position: absolute; left: 6px; top: 14px; width: 10px; height: 650px; }
  .bunting { position: absolute; left: 0; top: 0; width: 472px; height: 120px; }
  .sheet-title {
    position: absolute; top: 17px; left: 0; width: 100%;
    text-align: center;
    font-family: "Montserrat", sans-serif; font-weight: 700;
    font-size: 12.5px; letter-spacing: 0.6px; color: var(--ink);
  }
  .date-field {
    position: absolute; right: 11px; top: 96px;
    font-family: "Arimo", sans-serif; font-size: 10px; color: var(--ink);
  }
  .date-field .blank {
    display: inline-block; width: 46px; border-bottom: 1px solid var(--ink);
    margin-left: 3px;
  }
  .prompt {
    position: absolute; left: 47px;
    font-family: "Arimo", sans-serif; font-size: 12.5px; color: var(--ink);
  }
  .prompt--strengths { top: 155px; }
  .prompt--target { top: 245px; }
  .prompt--action { top: 348px; }
  .prompt--student { top: 453px; }
  .prompt--teacher { top: 565px; }
</style>
</head>
<body>
  <div class="sticker">
    <div class="sheet">
      <svg class="header-arc" viewBox="0 0 472 120" aria-hidden="true">
        <path d="M0 0 H472 V4 Q236 134 0 4 Z" fill="var(--paper-light)"/>
      </svg>

      <svg class="binding" viewBox="0 0 10 650" aria-hidden="true">
        <defs>
          <pattern id="binding-dots" width="10" height="21.5" patternUnits="userSpaceOnUse">
            <circle cx="5" cy="5" r="3.4" fill="var(--binding)"/>
            <line x1="5" y1="5" x2="10" y2="5" stroke="var(--binding)" stroke-width="1"/>
          </pattern>
        </defs>
        <rect width="10" height="650" fill="url(#binding-dots)"/>
      </svg>

      <svg class="bunting" viewBox="0 0 472 120" role="img" aria-label="Bunting of coloured triangular flags hanging along the header curve">
        <defs>
          <linearGradient id="bunting-tone" x1="0" y1="0" x2="1" y2="0">
            <stop offset="0" stop-color="var(--flag-tone-b)"/>
            <stop offset="1" stop-color="var(--flag-tone-a)"/>
          </linearGradient>
        </defs>
        <path d="M21 37 Q236 116 453 12 V44 Q236 146 21 85 Z" fill="url(#bunting-tone)" opacity="0.75"/>
        <path d="M0 4 Q236 134 472 4" fill="none" stroke="var(--arc)" stroke-width="2"/>
      </svg>

      <h1 class="sheet-title">FORMATIVE FEEDBACK Teacher C/L or H/L</h1>
      <p class="date-field">Date:<span class="blank"></span></p>

      <p class="prompt prompt--strengths">Strengths&nbsp; (What Went Well…)</p>
      <p class="prompt prompt--target">Target (Even Better If…)</p>
      <p class="prompt prompt--action">Action</p>
      <p class="prompt prompt--student">Response (from the student):</p>
      <p class="prompt prompt--teacher">Response and reflection (from the teacher):</p>
    </div>
  </div>
</body>
</html>
```